PRK website

Im a Specialty contractor that specializes in fireproofing. Epoxy flooring and terrazo along with poured floors and polished concrete.

We also do fire caulking.

Im the largest specialty flooring healthcare contractor in the south east.

Otto

Contractor

```html
<!DOCTYPE html>
<html lang="en">
<head>
<meta charset="utf-8">
<title>PRK – Specialty Flooring Contractor</title>
<link rel="stylesheet" href="https://fonts.googleapis.com/css2?family=Source+Sans+3:ital,wght@0,400;0,600;0,700;1,400&display=swap">
<style>
  :root {
    --sky-top: #8edbf0;
    --sky-bottom: #2bb4dc;
    --accent: #d9400f;
    --page: #24282b;
    --page-dark: #1e2124;
    --footer: #151617;
    --paper: #ddd5c7;
    --paper-side: #b1a898;
    --tab: #e2dbcd;
    --ink: #2c2a26;
    --ink-soft: #3a372f;
    --white: #ffffff;
    --frame: #efe9dc;
    --foot-text: #a9a9a9;
    --foot-muted: #5f6163;
    --foot-line: #2a2b2c;
  }
  * { margin: 0; padding: 0; box-sizing: border-box; }
  html, body { width: 873px; height: 1200px; overflow: hidden; }
  body {
    position: relative;
    font-family: "Source Sans 3", "Segoe UI", Arial, sans-serif;
    background: linear-gradient(180deg, var(--page) 0%, var(--page-dark) 100%);
    color: var(--ink);
  }

  /* Header */
  .site-header {
    position: absolute; left: 0; top: 0; width: 873px; height: 90px;
    background: linear-gradient(180deg, var(--sky-top) 0%, var(--sky-bottom) 100%);
    border-bottom: 7px solid var(--accent);
    box-shadow: 0 2px 4px rgba(0,0,0,.5);
  }
  .brand {
    position: absolute; left: 146px; top: 20px;
    font-size: 28px; font-weight: 700; letter-spacing: 1px; color: var(--white);
  }
  .search {
    position: absolute; left: 581px; top: 30px; width: 153px; height: 15px;
    background: #eef2f3; border: 1px solid #c9dce2;
    font-size: 12px; font-style: italic; color: #8a8f92; text-align: right;
    padding-right: 6px; line-height: 13px;
  }
  .main-nav { position: absolute; right: 139px; top: 56px; display: flex; }
  .main-nav a {
    color: var(--white); text-decoration: none; font-size: 13px; font-weight: 700;
    padding: 0 8px; line-height: 18px; border-left: 1px solid rgba(255,255,255,.45);
  }
  .main-nav a:first-child { border-left: 0; }
  .main-nav a:last-child { padding-right: 0; }

  /* Gallery */
  .gallery { position: absolute; left: 146px; top: 133px; display: flex; gap: 24px; }
  .gallery figure {
    width: 129px; height: 158px; background: var(--frame); padding: 6px;
    box-shadow: 0 2px 5px rgba(0,0,0,.6);
  }
  .gallery .swatch { width: 100%; height: 100%; }
  .swatch-hall { background: linear-gradient(160deg, #8a7c68 0%, #efe8dc 45%, #d8cbb8 100%); }
  .swatch-marble { background: radial-gradient(circle at 45% 45%, #c9863c 0%, #e6d9c2 55%, #efe6d6 100%); }
  .swatch-terrazzo-dark { background: radial-gradient(circle, #6e7073 0%, #3a3c3f 60%, #1b1c1e 100%); }
  .swatch-terrazzo-red { background: radial-gradient(circle at 40% 40%, #c98a73 0%, #a8614a 60%, #8a4a38 100%); }

  /* Content panel */
  .content-panel {
    position: absolute; left: 146px; top: 332px; width: 588px; height: 396px;
    background: var(--paper);
  }
  .intro { position: absolute; left: 0; top: 0; width: 409px; height: 396px; }
  .intro section { position: absolute; left: 12px; width: 390px; }
  .intro h2 { font-size: 15px; font-weight: 600; color: var(--ink); line-height: 18px; }
  .intro p {
    margin: 6px 0 0 9px; white-space: nowrap;
    font-size: 11px; line-height: 12.6px; color: var(--ink-soft);
  }
  .news {
    position: absolute; left: 409px; top: 0; width: 179px; height: 396px;
    background: var(--paper-side);
  }
  .news-item { position: absolute; left: 19px; width: 160px; }
  .news-item h3 {
    position: relative; width: 168px; height: 21px; background: var(--tab);
    font-size: 13px; font-weight: 700; line-height: 21px; padding-left: 8px; color: var(--ink);
    box-shadow: 0 1px 2px rgba(0,0,0,.25);
  }
  .news-item h3::after {
    content: ""; position: absolute; right: 0; bottom: -5px;
    border-top: 5px solid #7b7468; border-right: 8px solid transparent;
  }
  .news-item p {
    margin: 8px 0 0 10px; white-space: nowrap;
    font-size: 11px; line-height: 12.6px; color: var(--ink-soft);
  }
  .news-item .more {
    display: inline-block; margin: 2px 0 0 11px; padding: 0 2px;
    background: var(--tab); font-size: 10px; line-height: 11px; color: var(--ink);
  }

  /* Footer */
  .site-footer {
    position: absolute; left: 0; top: 778px; width: 873px; height: 422px;
    background: var(--footer);
  }
  .link-columns { position: absolute; left: 146px; top: 17px; width: 590px; }
  .link-col { position: absolute; top: 0; width: 148px; }
  .link-col h4 {
    font-size: 15px; font-weight: 600; color: var(--white); line-height: 22px;
    padding-bottom: 5px; border-bottom: 1px solid var(--foot-line);
  }
  .link-col ul { list-style: none; margin-top: 5px; }
  .link-col li { font-size: 13px; line-height: 21.9px; color: var(--foot-text); white-space: nowrap; }
  .legal {
    position: absolute; left: 146px; top: 338px; width: 588px; height: 50px;
    border-top: 1px solid var(--foot-line); border-bottom: 1px solid var(--foot-line);
    text-align: center; font-size: 11.5px; color: var(--foot-muted); white-space: nowrap;
  }
  .legal .copyright { margin-top: 5px; line-height: 16px; }
  .legal .policies { line-height: 18px; margin-top: 3px; }
</style>
</head>
<body>
  <header class="site-header">
    <div class="brand">PRK</div>
    <div class="search">search</div>
    <nav class="main-nav">
      <a href="#">Home</a>
      <a href="#">About Us</a>
      <a href="#">Services</a>
      <a href="#">Contact Us</a>
    </nav>
  </header>

  <div class="gallery">
    <figure><div class="swatch swatch-hall" role="img" aria-label="Photo of a polished floor in a bright corridor"></div></figure>
    <figure><div class="swatch swatch-marble" role="img" aria-label="Photo of cream stone surface with rust veining"></div></figure>
    <figure><div class="swatch swatch-terrazzo-dark" role="img" aria-label="Photo of dark terrazzo with grey chips"></div></figure>
    <figure><div class="swatch swatch-terrazzo-red" role="img" aria-label="Photo of red terrazzo flooring"></div></figure>
  </div>

  <main class="content-panel">
    <div class="intro">
      <section style="top:11px">
        <h2>Welcome to Company</h2>
        <p>Lorem ipsum dolor sit amet, consectetuer adipiscing elit, sed diam<br>nonummy nibh euismod tincidunt ut laoreet dolore magna aliquam<br>volutpat. Ut wisi enim ad minim veniam, quis nostrud exerci tation<br>ullamcorper suscipit lobortis nisl ut aliquip ex ea commodo consequat.</p>
      </section>
      <section style="top:116px">
        <h2>Products</h2>
        <p>Lorem ipsum dolor sit amet, consectetuer adipiscing elit, sed diam<br>nonummy nibh euismod tincidunt ut laoreet dolore magna aliquam<br>volutpat. Ut wisi enim ad minim veniam, quis nostrud exerci tation<br>ullamcorper suscipit lobortis nisl ut aliquip ex ea commodo consequat.</p>
      </section>
      <section style="top:212px">
        <h2>Services</h2>
        <p>Lorem ipsum dolor sit amet, consectetuer adipiscing elit, sed diam<br>nonummy nibh euismod tincidunt ut laoreet dolore magna aliquam<br>volutpat. Ut wisi enim ad minim veniam, quis nostrud exerci tation<br>ullamcorper suscipit lobortis nisl ut aliquip ex ea commodo consequat.</p>
      </section>
      <section style="top:309px">
        <h2>Why Us ?</h2>
        <p>Lorem ipsum dolor sit amet, consectetuer adipiscing elit, sed diam<br>nonummy nibh euismod tincidunt ut laoreet dolore magna aliquam<br>volutpat. Ut wisi enim ad minim veniam, quis nostrud exerci tation<br>ullamcorper suscipit lobortis nisl ut aliquip ex ea commodo consequat.</p>
      </section>
    </div>

    <aside class="news">
      <article class="news-item" style="top:11px">
        <h3>Latest News One</h3>
        <p>Lorem ipsum dolor sit amet,<br>consectetuer adipiscing elit,<br>sed diam nonummy nibh<br>euismod tincidunt ut laoreet<br>dolore magna aliquam...</p>
        <span class="more">more</span>
      </article>
      <article class="news-item" style="top:136px">
        <h3>Latest News One</h3>
        <p>Lorem ipsum dolor sit amet,<br>consectetuer adipiscing elit,<br>sed diam nonummy nibh<br>euismod tincidunt ut laoreet<br>dolore magna aliquam...</p>
        <span class="more">more</span>
      </article>
      <article class="news-item" style="top:260px">
        <h3>Latest News One</h3>
        <p>Lorem ipsum dolor sit amet,<br>consectetuer adipiscing elit,<br>sed diam nonummy nibh<br>euismod tincidunt ut laoreet<br>dolore magna aliquam...</p>
        <span class="more">more</span>
      </article>
    </aside>
  </main>

  <footer class="site-footer">
    <div class="link-columns">
      <div class="link-col" style="left:0">
        <h4>Popular Search</h4>
        <ul><li>Flooring</li><li>Fireproofing</li><li>terrazo</li><li>polished concrete.</li><li>Flooring</li><li>Fireproofing</li><li>terrazo</li><li>polished concrete.</li><li>Flooring</li><li>Fireproofing</li><li>terrazo</li><li>polished concrete.</li></ul>
      </div>
      <div class="link-col" style="left:162px">
        <h4>Popular Search</h4>
        <ul><li>Flooring</li><li>Fireproofing</li><li>terrazo</li><li>polished concrete.</li><li>Flooring</li><li>Fireproofing</li><li>terrazo</li><li>polished concrete.</li><li>Flooring</li><li>Fireproofing</li><li>terrazo</li><li>polished concrete.</li></ul>
      </div>
      <div class="link-col" style="left:325px">
        <h4>Popular Search</h4>
        <ul><li>Flooring</li><li>Fireproofing</li><li>terrazo</li><li>polished concrete.</li><li>Flooring</li><li>Fireproofing</li><li>terrazo</li><li>polished concrete.</li><li>Flooring</li><li>Fireproofing</li><li>terrazo</li><li>polished concrete.</li></ul>
      </div>
      <div class="link-col" style="left:487px; width:101px">
        <h4>Popular Search</h4>
        <ul><li>Flooring</li><li>Fireproofing</li><li>terrazo</li><li>polished concrete.</li><li>Flooring</li><li>Fireproofing</li><li>terrazo</li><li>polished concrete.</li><li>Flooring</li><li>Fireproofing</li><li>terrazo</li><li>polished concrete.</li></ul>
      </div>
    </div>
    <div class="legal">
      <p class="copyright">Copyright 2012 &nbsp;|&nbsp; All Rights Reserved</p>
      <p class="policies">Anti-spam policy | Disclaimer | Dmca notice | Email Policy | Earnings Disclaimer | External Links Policy | Testimonials</p>
    </div>
  </footer>
</body>
</html>
```